Veltrano Energy Business Card Design

website: www.veltranoenergy.example
Project: Business Card Design for Veltrano Energy
Name: Dorian Kettle
Title: Founder / Operations Strategist
Visual Identity & Logo:
Logo File: VEL-Logo-FullGradient-Final.png (Attached).
Color Palette: The brand relies on a distinctive Cyan (Blue) to Lime Green gradient.
Background Preference: We want a Dark Mode aesthetic (Deep Matte Black, Charcoal, or Dark Slate) to make the neon gradient of the logo pop. This feels more "tech/industrial" than a standard white card.
Design Aesthetic (The "Ops" Vibe):
Concept: "Grid & Infrastructure." We are a solar rental company, focusing on logistics and access.
Typography: White, bold sans-serif text for contact info. High contrast against the dark background.
Accents: Use the Cyan or Lime Green from the logo for thin divider lines or edge painting.
Avoid: No orange/gold (clashes with logo). No cartoon leaves.
Layout Requirements:
Front: Large, centered logo. Maybe a subtle UV gloss spot varnish over the logo icon.
Back: Name, Title, Contact Info.
Texture: Matte finish cardstock with gloss elements.
sample mock up of information on card: https://brivomarkco-my.filehost.example/:i:/g/personal/dorian_kettle_veltranoenergy_example/AbCdEfGhIjKlMnOpQrStUvWxYz012345678?e=Xy12Ab
Logo: https://brivomarkco.filehost.example/:i:/s/VeltranoEnergy/ZyXwVuTsRqPoNmLkJiHgFeDcBa9876543210?e=Pq34Cd

```html
<!DOCTYPE html>
<html lang="en">
<head>
<meta charset="utf-8">
<title>Veltrano Energy — Business Card</title>
<link href="https://fonts.googleapis.com/css2?family=Outfit:wght@300;400;500&display=swap" rel="stylesheet">
<style>
  :root {
    --page: #ffffff;
    --card: #373e44;
    --ink: #ffffff;
    --cyan: #12a0d8;
    --teal: #3bb7a8;
    --lime: #b5d334;
    --shadow: rgba(0, 0, 0, 0.28);
  }
  * { margin: 0; padding: 0; box-sizing: border-box; }
  html, body {
    width: 989px;
    height: 1200px;
    overflow: hidden;
    background: var(--page);
    font-family: "Outfit", sans-serif;
  }
  .card {
    position: absolute;
    left: 151px;
    width: 680px;
    height: 389px;
    background: var(--card);
    border-radius: 9px;
    overflow: hidden;
    box-shadow: 14px 16px 26px var(--shadow);
    color: var(--ink);
  }
  .card--contact { top: 158px; }
  .card--brand { top: 644px; }

  /* thin edge painting */
  .edge-line {
    position: absolute;
    background: linear-gradient(180deg, var(--cyan), var(--lime));
  }
  .edge-line--left { left: 0; top: 0; bottom: 0; width: 5px; }
  .edge-line--bottom {
    left: 0; right: 0; bottom: 0; height: 5px;
    background: linear-gradient(90deg, var(--cyan), var(--lime));
  }

  .person {
    position: absolute;
    left: 37px;
    top: 55px;
  }
  .person__name {
    font-size: 35px;
    font-weight: 500;
    letter-spacing: 0.2px;
    line-height: 1;
  }
  .person__title {
    margin-top: 14px;
    font-size: 17px;
    font-weight: 400;
    letter-spacing: 0.2px;
  }
  .divider {
    position: absolute;
    left: 37px;
    top: 150px;
    width: 64px;
    height: 2px;
    background: var(--lime);
  }
  .contact {
    position: absolute;
    left: 37px;
    top: 185px;
    list-style: none;
    font-size: 19px;
    font-weight: 400;
    letter-spacing: 0.3px;
  }
  .contact li { line-height: 25px; margin-bottom: 12px; }
  .contact .contact__address { margin-bottom: 0; }

  .wordmark-side {
    position: absolute;
    left: 430px;
    top: 188px;
    display: flex;
    align-items: center;
    gap: 12px;
  }
  .brand-square {
    width: 24px;
    height: 24px;
    background: var(--cyan);
    border-radius: 3px;
  }
  .brand-name {
    font-weight: 400;
    color: var(--teal);
    line-height: 1;
  }
  .wordmark-side .brand-name { font-size: 38px; }

  .wordmark-center {
    position: absolute;
    left: 0; right: 0;
    top: 160px;
    display: flex;
    justify-content: center;
    align-items: center;
    gap: 18px;
  }
  .wordmark-center .brand-square { width: 54px; height: 54px; border-radius: 5px; }
  .wordmark-center .brand-name { font-size: 60px; font-weight: 300; }
</style>
</head>
<body>
  <section class="card card--contact" aria-label="Card contact side">
    <div class="edge-line edge-line--left"></div>

    <div class="person">
      <h1 class="person__name">Dorian Kettle</h1>
      <p class="person__title">Founder / Operations Strategist</p>
    </div>
    <div class="divider"></div>

    <ul class="contact">
      <li>555-014-2287</li>
      <li>www.veltranoenergy.example</li>
      <li class="contact__address">4120 Harbor Fern Lane<br>Lakeview, ST 10482</li>
    </ul>

    <div class="wordmark-side">
      <span class="brand-square"></span>
      <span class="brand-name">Veltrano</span>
    </div>
  </section>

  <section class="card card--brand" aria-label="Card brand side">
    <div class="edge-line edge-line--bottom"></div>

    <div class="wordmark-center">
      <span class="brand-square"></span>
      <span class="brand-name">Veltrano Energy</span>
    </div>
  </section>
</body>
</html>
```